Open House evite for our 7th Anniversary needs Invitation Design

Need an invitation design for an upcoming event. Our event is an Open House to celebrate our 7th anniversary with clients & business colleagues. We need a professional but fun invitation. We are a women owned law firm. We will use this design for a Save the Date, an evite, a hard invitation, an eReminder and a wine label.
Focus of design should be on the "7"!!! (this is new)
Every year the focus will be on the year.
We have 3 women partners who run the firm. If there is a way to incorporate that into the drawing-great! Attached is a sketch that focuses on the 7 and has three stick figure women. It has our logo "&" in the background and says "Seven Lucky Years & Still Going...." OPEN HOUSE....This is a thought, please play around with it. It does not have to have the women, but is one thought. We have a submittal on an elegant 7 that we liked, but did not hear back from the designer, so that is an option also. An elegant 7 in black, gray background, with blue or green as accent colors is something else we would like to see.

Please view our website: www.bhqcounsel.example for our colors. You do not need to use these, but it gives you an idea of the feel of our marketing.
Incorporate:
our logo, per attached

OPEN HOUSE:
June 4, 2015
3:00-7:00pm
Brenner, Hollis & Quade, LLC
4812 Tamarack, Suite 410
Linden Falls, IL 60999
RSVP to rsvp@bhqcounsel.example

We will only be sending out about 20 actual hard copy invites. We will be sending the evites through Steady Mailer and this is the heart of the project. We will send a Save the Date, then 2-3 weeks later an evite, then 2-4 weeks later a Reminder, and then the week before one more reminder.
The wine labels are used all year long and are the past years are all displayed in frames in our office. They are an important aspect of our marketing efforts.

Target Market(s)

Adults - clients & business colleagues

Industry/Entity Type

Business

Colors
000000
acd036
81c7e5

Requirements
Must have
• Focus the design on the "7". There is a sketched attached. This is not exactly what we want, but a thought. See attached.
• Incorporate our logo, per attached
• OPEN HOUSE:
• June 4, 2015
• 3:00-7:00pm
• Brenner, Hollis & Quade, LLC
• 4812 Tamarack, Suite 410
• Linden Falls, IL 60999
• RSVP to rsvp@bhqcounsel.example
Nice to have
• If you can incorporate 3 women lawyer figures into the design - great! Stick figures are ok.

```html
<!DOCTYPE html>
<html lang="en">
<head>
<meta charset="utf-8">
<title>Lucky – Open House Invitation</title>
<link href="https://fonts.googleapis.com/css2?family=Playfair+Display:wght@400&display=swap" rel="stylesheet">
<style>
  :root {
    --blue-deep: #0099d8;
    --blue-light: #1cb1e2;
    --green: #b7d87b;
    --white: #ffffff;
    --ink: #5d5d5d;
    --logo-ink: #3a3f4a;
  }
  * { margin: 0; padding: 0; box-sizing: border-box; }
  html, body {
    width: 873px;
    height: 1200px;
    overflow: hidden;
    background: var(--white);
  }
  .invitation {
    position: relative;
    width: 873px;
    height: 1200px;
    overflow: hidden;
    background: var(--white);
    font-family: "Playfair Display", Georgia, serif;
    font-variant-numeric: lining-nums;
  }
  .backdrop {
    position: absolute;
    inset: 0;
    display: block;
  }
  .headline {
    position: absolute;
    left: 40px;
    top: 262px;
    color: var(--white);
    font-size: 124px;
    font-weight: 400;
    letter-spacing: 7px;
    line-height: 1;
  }
  .event-details {
    position: absolute;
    right: 33px;
    top: 830px;
    text-align: right;
  }
  .event-title {
    color: var(--white);
    font-size: 44px;
    font-weight: 400;
    letter-spacing: 2.5px;
    line-height: 1;
    margin-bottom: 14px;
  }
  .event-line {
    color: var(--ink);
    font-size: 21px;
    letter-spacing: 1.6px;
    line-height: 37px;
  }
  .firm-mark {
    position: absolute;
    left: 160px;
    top: 1130px;
    display: flex;
    align-items: center;
    gap: 8px;
  }
  .firm-mark-dot {
    width: 11px;
    height: 11px;
    border-radius: 50%;
    background: var(--logo-ink);
  }
  .firm-mark-name {
    color: var(--logo-ink);
    font-size: 15px;
    letter-spacing: 0.4px;
  }
</style>
</head>
<body>
  <main class="invitation">
    <svg class="backdrop" width="873" height="1200" viewBox="0 0 576 792" preserveAspectRatio="none" aria-hidden="true">
      <polygon class="seven-stroke" points="0,173 341,173 40,792 0,792" fill="var(--blue-deep)"/>
      <polygon class="seven-inner" points="0,283 237,283 0,770" fill="var(--blue-light)"/>
      <polygon class="accent-wedge" points="576,50 576,792 222,792" fill="var(--green)"/>
    </svg>

    <h1 class="headline">Lucky</h1>

    <section class="event-details">
      <h2 class="event-title">Open House</h2>
      <p class="event-line">June 4, 2015</p>
      <p class="event-line">3:00-7:00pm</p>
      <p class="event-line">Brenner, Hollis &amp; Quade, LLC</p>
      <p class="event-line">4812 Tamarack, Suite 410</p>
      <p class="event-line">Linden Falls, IL 60999</p>
      <p class="event-line">RSVP to rsvp@bhqcounsel.example</p>
    </section>

    <div class="firm-mark">
      <span class="firm-mark-dot"></span>
      <span class="firm-mark-name">Brenner Hollis Quade</span>
    </div>
  </main>
</body>
</html>
```